Bright Arrow Delivery Service Wordpress design

My client is a delivery service whose motto is "We go where the freight leads us." Their colors are red, white and blue. They use Voyalo vans and box vans - NO semi tractors. They like this Website design www.tovamu-sample.com, but I would like to see some designs that make them stand out. Attached is their new logo.

Target Market(s)

Businesses who use delivery services in town and anyone needing freight picked up or transported in the United States.

Industry/Entity Type

Delivery Service

Number of Pages Required

1 page

Font styles to use
Sans Serif

Colors
ec1f27
0455a3
ffffff

Requirements
Must have
• We need a Wordpress design with sliders that incorporates their new logo and the motto "WE GO WHERE THE FREIGHT LEADS US" Their corporate colors are red, white and blue. They only use voyalo vans and box vans.
Nice to have
• Please use your creativity to come up with a unique design for this delivery service.
Should not have
• NO SEMI TRACTOR TRAILERS

```html
<!DOCTYPE html>
<html lang="en">
<head>
<meta charset="utf-8">
<title>Bright Arrow Delivery Service</title>
<link href="https://fonts.googleapis.com/css2?family=PT+Sans:wght@400;700&family=Open+Sans:wght@300;400;600;700;800&family=Oswald:wght@300;500&family=Lobster&display=swap" rel="stylesheet">
<style>
:root{
  --red:#ec1f27;
  --red-dark:#9e0f14;
  --blue:#0455a3;
  --navy:#1a1a6b;
  --white:#ffffff;
  --page:#f3f3f3;
  --text:#8a8a8a;
  --nav:#555555;
  --gold:#f0b21a;
  --orange:#f39a1e;
  --footer:#161616;
}
*{margin:0;padding:0;box-sizing:border-box}
html,body{width:1025px;height:1200px;overflow:hidden}
body{background:var(--page);font-family:'PT Sans',sans-serif;position:relative}
.topline{position:absolute;left:0;top:0;width:1025px;height:5px;background:var(--navy)}
.header{position:absolute;left:0;top:5px;width:1025px;height:86px;background:var(--page)}
.logo{position:absolute;left:122px;top:38px;display:flex;align-items:center;gap:10px}
.logo-name{font-family:'PT Sans',sans-serif;font-weight:700;font-size:24px;color:var(--navy);letter-spacing:1px}
.logo-mark{width:40px;height:40px;border-radius:50%;background:var(--navy)}
.client-register{position:absolute;left:726px;top:12px;font-size:13px;color:#555}
.login{position:absolute;left:814px;top:5px;width:85px;height:28px;background:var(--navy);border-radius:0 0 5px 5px;color:var(--white);font-weight:700;font-size:12px;display:flex;align-items:center;justify-content:center;gap:5px}
.nav{position:absolute;top:58px;left:0;width:1025px}
.nav a{position:absolute;font-size:12.5px;font-weight:700;color:var(--nav);text-decoration:none;letter-spacing:.2px}
.nav a.active{color:var(--red)}
.nav a.active::after{content:"";position:absolute;left:0;right:0;top:29px;height:2px;background:var(--red)}
.hero{position:absolute;left:0;top:91px;width:1025px;height:367px;background:radial-gradient(ellipse 380px 160px at 512px 60px,#f3a94a 0%,#f07a2c 40%,var(--red) 90%)}
.motto{position:absolute;top:120px;left:0;width:1025px;text-align:center;font-family:'Lobster',cursive;font-size:27px;color:var(--white);text-shadow:0 1px 2px rgba(0,0,0,.2)}
.motto span{color:#2a1a12}
.slider{position:absolute;left:122px;top:174px;width:777px;height:322px;background:var(--white);padding:6px}
.slide{width:100%;height:100%;background:linear-gradient(180deg,#7a8a3a 0%,#9aa04a 35%,#6b6b68 70%,#5a5a58 100%)}
.dots{position:absolute;left:0;top:289px;width:100%;display:flex;justify-content:center;gap:4px;transform:translateX(-124px)}
.dots i{width:14px;height:14px;border-radius:50%;background:#d8d8d8;border:2px solid var(--white)}
.dots i.on{background:var(--red)}
.card{position:absolute;top:522px;width:234px;height:181px;border-radius:7px;box-shadow:0 8px 10px -6px rgba(0,0,0,.35);overflow:hidden}
.card .icon{position:absolute;left:24px;top:24px;width:70px;height:78px;border-radius:8px}
.card h3{position:absolute;right:22px;top:18px;text-align:right;font-family:'Open Sans',sans-serif;font-weight:400;font-size:24px;line-height:25px;color:var(--white)}
.card h3 b{display:block;font-weight:700;font-size:26px;margin-top:6px}
.card .strip{position:absolute;left:7px;right:7px;bottom:7px;height:50px;border-radius:0 0 4px 4px;display:flex;align-items:center;justify-content:space-between;padding:0 10px 0 14px}
.card .strip p{font-family:'Oswald',sans-serif;font-weight:300;font-size:9.5px;line-height:12px;letter-spacing:.2px}
.card .btn{font-family:'PT Sans',sans-serif;font-weight:700;font-size:11.5px;color:var(--white);padding:6px 10px;border-radius:2px}
.card.gifts{left:126px;background:linear-gradient(180deg,#f7c325,#eba312)}
.card.gifts .icon{background:#e46a20}
.card.gifts h3{color:#9c1014}
.card.gifts h3 b{color:var(--white)}
.card.gifts .strip{background:#7d1512}
.card.gifts .strip p{color:var(--white)}
.card.gifts .btn{background:#d9861a}
.card.medical{left:394px;background:linear-gradient(180deg,#1c8ee0,var(--blue))}
.card.medical .icon{background:#9a5a1a}
.card.medical h3 b{color:var(--gold)}
.card.medical .strip{background:#f6c44c}
.card.medical .strip p{color:#3a2a10}
.card.medical .btn{background:var(--blue)}
.card.techie{left:662px;background:linear-gradient(180deg,#c8141c,#8e0b10)}
.card.techie .icon{background:#f0d420;border-radius:50%}
.card.techie h3 b{color:var(--gold)}
.card.techie .strip{background:#f6c44c}
.card.techie .strip p{color:#3a2a10}
.card.techie .btn{background:#4a0a0a}
.welcome{position:absolute;top:760px;left:0;width:1025px;text-align:center;font-family:'Open Sans',sans-serif;font-weight:300;font-size:27px;color:#444;letter-spacing:-.5px}
.welcome b{color:var(--red);font-weight:700}
.rule{position:absolute;top:778px;width:122px;border-top:2px dotted #cfcfcf}
.intro{position:absolute;top:815px;left:190px;width:645px;text-align:center;font-family:'Open Sans',sans-serif;font-size:9.6px;line-height:14.5px;color:var(--text)}
.intro p+p{margin-top:8px}
.callbar{position:absolute;left:0;top:964px;width:1025px;height:60px;background:var(--red);display:flex;align-items:center;justify-content:center;gap:10px;color:var(--white);font-family:'Oswald',sans-serif}
.callbar .label{font-weight:300;font-size:17px}
.callbar .nums{font-weight:500;font-size:19px;letter-spacing:.3px}
.footer{position:absolute;left:0;top:1024px;width:1025px;height:176px;background:radial-gradient(ellipse 420px 80px at 330px 0,#4a4242,var(--footer) 100%)}
.footer h4{position:absolute;left:124px;top:28px;font-size:10.5px;color:#aaa;text-decoration:underline;font-weight:700}
.footer .about{position:absolute;left:124px;top:50px;width:310px;font-size:8.6px;line-height:12.8px;color:#bbb}
.footer-nav{position:absolute;left:507px;top:28px;display:flex;gap:20px;font-size:10.5px;font-weight:700;color:#888}
.footer-nav .active{color:#ccc;text-decoration:underline}
.legal{position:absolute;left:507px;top:56px;font-size:10px;color:#999;letter-spacing:.3px}
.social{position:absolute;left:688px;top:53px;display:flex;gap:6px}
.social i{width:20px;height:20px;border-radius:50%;background:#777}
.social i.on{background:var(--red)}
</style>
</head>
<body>
<div class="topline"></div>
<header class="header">
  <div class="logo" style="top:28px"><span class="logo-name">BRIGHT ARROW</span><span class="logo-mark"></span></div>
  <span class="client-register">Client Register</span>
  <span class="login">Login
    <svg width="11" height="11" viewBox="0 0 12 12"><path d="M3 5V3.5a3 3 0 0 1 6 0V5" fill="none" stroke="#fff" stroke-width="1.6"/><rect x="1.5" y="5" width="9" height="7" rx="1" fill="#fff"/></svg>
  </span>
</header>
<nav class="nav">
  <a class="active" style="left:502px">HOME</a>
  <a style="left:558px">COURIER</a>
  <a style="left:629px">FREIGHT</a>
  <a style="left:699px">ABOUT</a>
  <a style="left:760px">CAREER</a>
  <a style="left:825px">CONTACTS</a>
</nav>
<section class="hero">
</section>
<h1 class="motto">We go where <span>the Freight leads us</span></h1>
<div class="slider">
  <div class="slide" role="img" aria-label="Smiling courier in shirt and tie presenting a white Voyalo van on a winding autumn forest road"></div>
  <div class="dots"><i class="on"></i><i></i><i></i></div>
</div>
<div class="card gifts">
  <div class="icon" role="img" aria-label="Wrapped gift box with red ribbon"></div>
  <h3>Valuable<br>Items<b>GIFTS</b></h3>
  <div class="strip"><p>Lorem ipsum sit amet,<br>consectetur elit.</p><span class="btn">Read More</span></div>
</div>
<div class="card medical">
  <div class="icon" role="img" aria-label="Brown leather briefcase"></div>
  <h3>Quick<br>Delivery<b>MEDICAL</b></h3>
  <div class="strip"><p>Lorem ipsum sit amet,<br>consectetur elit.</p><span class="btn">Read More</span></div>
</div>
<div class="card techie">
  <div class="icon" role="img" aria-label="Glowing yellow light bulb"></div>
  <h3>Online<br>Tracking<b>TECHIE</b></h3>
  <div class="strip"><p>Lorem ipsum sit amet,<br>consectetur elit.</p><span class="btn">Read More</span></div>
</div>
<div class="rule" style="left:231px"></div>
<div class="rule" style="left:663px"></div>
<h2 class="welcome"><b>WELCOME</b> TO OUR SITE</h2>
<div class="intro">
  <p>Lorem ipsum dolor sit amet, consectetur adipisicing elit, sed do eiusmod tempor incididunt ut labore et dolore magna aliqua. Ut enim ad minim veniam, quis nostrud exercitation ullamco laboris nisi ut aliquip ex ea commodo consequat. Duis aute irure dolor in reprehenderit in voluptate velit.</p>
  <p>Lorem ipsum dolor sit amet, consectetur adipisicing elit, sed do eiusmod tempor incididunt ut labore et dolore magna aliqua. Ut enim ad minim veniam, quis nostrud exercitation ullamco laboris nisi ut aliquip ex ea commodo consequat. Duis aute irure dolor in reprehenderit in voluptate velit esse cillum dolore fugiat nulla pariatur. Excepteur sint occaecat cupidatat non proident, sunt in culpa qui officia deserunt mollit anim id est laborum laborum. orem ipsum dolor sit amet, consectetur adipisicing elit, sed do eiusmod tempor incididunt.</p>
</div>
<div class="callbar">
  <span class="label">Call Us</span>
  <svg width="28" height="28" viewBox="0 0 28 28"><circle cx="14" cy="14" r="12.5" fill="none" stroke="#fff" stroke-width="2"/><path d="M10 7.5l2.5 3-1.6 1.8c.8 2 2.3 3.5 4.3 4.4l1.8-1.6 3 2.5-1.5 2.4c-5 0-10.5-5.4-10.5-10.5z" fill="#fff"/></svg>
  <span class="nums">555-210-4417 / 555-210-4419 / 555-210-8830</span>
</div>
<footer class="footer">
  <h4>About Us</h4>
  <p class="about">Lorem ipsum dolor sit amet, consectetur adipisicing elit, sed do eiusmod tempor incididunt ut labore et dolore magna aliqua. Ut enim ad minim veniam, quis nostrud exercitation ullamco laboris nisi ut aliquip ex ea commodo consequat. Duis aute irure dolor in reprehenderit in voluptate velit.</p>
  <div class="footer-nav"><span class="active">Home</span><span>Courier</span><span>Freight</span><span>About</span><span>Career</span><span>Contacts</span></div>
  <div class="legal">Terms &amp; Policy. Copyright © 2016</div>
  <div class="social"><i></i><i class="on"></i><i></i></div>
</footer>
</body>
</html>
```